Private Gym Needs a Rack Card Design

We need a basic front and back rack card (same size as post card) that gives basic information about our brand, and includes our logo. Please see attached logo and required content below.

Target Market(s)

Upscale, private gym.

Industry/Entity Type

Gym

Font styles to use
Sans Serif

Colors
ffffff
5c5c5c
000000
dbdbdb
f78f20

Requirements
Must have
• Business Logo and the following text in a clean, modern, easy-to-read, artistic manner. Style and design must be clean, incorporate our color scheme of MOSTLY white, light grey, charcoal, with just pops of orange. We want the card itself to be mostly white background. Must include website URL as well: corevaultfitness.com
• FRONT CARD:
• Logo
• A safe and individualized approach to exercise
• our path employs the latest weight resistance training exercises and coaching for healthy living. Not only is our workout methodology effective, it’s safe.
• Our Path…
• -Improves Functional Movement
• -Promotes Weight Loss
• -Builds Strength
• -Increases Flexibility 

• BACK:
• Change Your Body. Find Your Strength.
• There’s 40 years of success behind our proven method
• What is Iron Path? 
• Iron Path is all about teaching our clients how to lift weights and exercise with the proper technique. There’s no slinging or jerking at our gym; only controlled movements that yield real results.
• Come workout with us in our private gym. We are located in Durham adjacent to Larch Campus and 5 minutes from downtown Durham.
• Address: 482 Fenwick Ave, Durham, NC 27705
• Phone: (919) 555-0147
• Hours: 9:00 AM – 9:00 PM
Nice to have
• Great organization of text, maybe some columns, colored bullet points, cool graphics and logos.
Should not have
• Busy or crowded design. All lines should be sleek, straight, and streamline. NO STOCK IMAGES, but logos are GREAT

```html
<!DOCTYPE html>
<html lang="en">
<head>
<meta charset="utf-8">
<title>Iron Path Rack Cards</title>
<link rel="stylesheet" href="https://fonts.googleapis.com/css2?family=Open+Sans:ital,wght@0,400;0,600;0,700;0,800;1,400&display=swap">
<style>
  :root {
    --orange: #f26638;
    --charcoal: #545456;
    --text: #2b2b2b;
    --footer-grey: #a7a8aa;
    --white: #ffffff;
    --backdrop: #ecebea;
    --panel-dark: #1c1c1c;
  }
  * { box-sizing: border-box; margin: 0; padding: 0; }
  html, body {
    width: 1165px; height: 1200px; overflow: hidden;
    background: var(--backdrop);
    font-family: "Open Sans", Arial, sans-serif;
    color: var(--text);
  }
  .canvas { position: relative; width: 1165px; height: 1200px; }
  .rack-card {
    position: absolute; width: 469px; height: 1030px;
    background: var(--white);
    display: flex; flex-direction: column;
    box-shadow: 0 4px 14px rgba(0,0,0,0.18);
  }
  .rack-card--front { left: 72px; top: 69px; }
  .rack-card--back { left: 617px; top: 99px; }

  .header-band { color: var(--white); }
  .header-band--orange {
    background: var(--orange); height: 131px;
    display: flex; align-items: center; justify-content: center; text-align: center;
  }
  .header-title { font-weight: 700; font-size: 25px; line-height: 35px; letter-spacing: 0.3px; }
  .header-band--charcoal { background: var(--charcoal); height: 130px; padding: 26px 20px 0; }
  .headline { font-size: 24px; font-weight: 600; line-height: 32px; }
  .subline { font-size: 16px; font-style: italic; margin-top: 6px; }

  .copy { padding: 14px 20px 0; }
  .copy--front { height: 272px; }
  .copy--back { height: 177px; padding-top: 28px; }
  .body-text { font-size: 15px; line-height: 23px; text-align: justify; hyphens: auto; -webkit-hyphens: auto; }
  .section-title { color: var(--orange); font-size: 18.5px; font-weight: 400; margin: 26px 0 10px; }
  .copy--back .section-title { margin: 0 0 12px; }
  .benefit-list { list-style: none; }
  .benefit-list li { font-size: 16px; line-height: 28px; display: flex; align-items: center; gap: 8px; }
  .benefit-list svg { flex: none; }

  .image-area { background: var(--panel-dark); }
  .image-area--front { height: 383px; }
  .image-area--back { height: 340px; }

  .visit-band {
    background: var(--orange); color: var(--white); height: 144px;
    margin-top: 4px; text-align: center; padding-top: 22px;
    font-size: 15.5px; line-height: 23px;
  }
  .visit-band .hours { color: var(--text); font-weight: 700; font-size: 15px; margin-top: 8px; }

  .brand-area { flex: 1; display: flex; align-items: center; justify-content: center; gap: 12px; }
  .brand-mark { width: 20px; height: 20px; background: var(--orange); }
  .brand-name { font-size: 40px; font-weight: 800; color: var(--charcoal); letter-spacing: 1px; }

  .contact-band {
    background: var(--footer-grey); color: var(--white); height: 88px;
    text-align: center; padding-top: 9px;
  }
  .contact-phone { font-size: 20px; font-weight: 700; line-height: 26px; display: flex; justify-content: center; align-items: center; gap: 10px; }
  .contact-address, .contact-web { font-size: 14.5px; font-weight: 700; line-height: 22px; }
</style>
</head>
<body>
<div class="canvas">

  <section class="rack-card rack-card--front">
    <header class="header-band header-band--orange">
      <h1 class="header-title">A SAFE AND INDIVIDUALIZED<br>APPROACH TO EXERCISE</h1>
    </header>
    <div class="copy copy--front">
      <p class="body-text">Our path employs the latest weight resistance training exercises and coaching for healthy living. Not only is our workout methodology effective, it’s safe.</p>
      <h2 class="section-title">Our Path...</h2>
      <ul class="benefit-list">
        <li><svg width="12" height="14" viewBox="0 0 12 14"><path d="M0 0 L12 7 L0 14 Z" fill="var(--orange)"/></svg>Improves Functional Movement</li>
        <li><svg width="12" height="14" viewBox="0 0 12 14"><path d="M0 0 L12 7 L0 14 Z" fill="var(--orange)"/></svg>Promotes Weight Loss</li>
        <li><svg width="12" height="14" viewBox="0 0 12 14"><path d="M0 0 L12 7 L0 14 Z" fill="var(--orange)"/></svg>Builds Strength</li>
        <li><svg width="12" height="14" viewBox="0 0 12 14"><path d="M0 0 L12 7 L0 14 Z" fill="var(--orange)"/></svg>Increases Flexibility</li>
      </ul>
    </div>
    <div class="image-area image-area--front" role="img" aria-label="Area for a dark training image of a barbell curl"></div>
    <div class="brand-area"><span class="brand-mark"></span><span class="brand-name">IRON PATH</span></div>
    <footer class="contact-band">
      <div class="contact-phone">
        <svg width="16" height="16" viewBox="0 0 24 24"><path fill="var(--white)" d="M6.6 10.8a15.1 15.1 0 0 0 6.6 6.6l2.2-2.2a1 1 0 0 1 1-.25 11.4 11.4 0 0 0 3.6.57 1 1 0 0 1 1 1V20a1 1 0 0 1-1 1A17 17 0 0 1 3 4a1 1 0 0 1 1-1h3.5a1 1 0 0 1 1 1c0 1.25.2 2.45.57 3.57a1 1 0 0 1-.25 1z"/></svg>
        (919) 555-0147
      </div>
      <div class="contact-address">482 Fenwick Ave, Durham, NC 27705</div>
      <div class="contact-web">corevaultfitness.com</div>
    </footer>
  </section>

  <section class="rack-card rack-card--back">
    <header class="header-band header-band--charcoal">
      <h1 class="headline">Change Your Body.<br>Find Your Strength.</h1>
      <p class="subline">There’s 40 years of success behind our proven method</p>
    </header>
    <div class="copy copy--back">
      <h2 class="section-title">What is Iron Path?</h2>
      <p class="body-text">Iron Path is all about teaching our clients how to lift weights and exercise with the proper technique. There’s no slinging or jerking at our gym; only controlled movements that yield real results.</p>
    </div>
    <div class="image-area image-area--back" role="img" aria-label="Area for a dark training image of a dumbbell lift"></div>
    <div class="visit-band">
      <p>Come workout with us in our private gym.<br>We are located in Durham adjacent to Larch Campus<br>and 5 minutes from downtown Durham.</p>
      <p class="hours">Hours: 9:00 AM – 9:00 PM</p>
    </div>
    <div class="brand-area"><span class="brand-mark"></span><span class="brand-name">IRON PATH</span></div>
    <footer class="contact-band">
      <div class="contact-phone">
        <svg width="16" height="16" viewBox="0 0 24 24"><path fill="var(--white)" d="M6.6 10.8a15.1 15.1 0 0 0 6.6 6.6l2.2-2.2a1 1 0 0 1 1-.25 11.4 11.4 0 0 0 3.6.57 1 1 0 0 1 1 1V20a1 1 0 0 1-1 1A17 17 0 0 1 3 4a1 1 0 0 1 1-1h3.5a1 1 0 0 1 1 1c0 1.25.2 2.45.57 3.57a1 1 0 0 1-.25 1z"/></svg>
        (919) 555-0147
      </div>
      <div class="contact-address">482 Fenwick Ave, Durham, NC 27705</div>
      <div class="contact-web">corevaultfitness.com</div>
    </footer>
  </section>

</div>
</body>
</html>
```